bright-vale.net Real Estate, Investment, Financial corporate

Real Estate, Investment, Financial corporate looking site. Show present a professional firm, with an elegant display. Please see the attached file which includes the logo, palette and fonts.
Updates

We just starting the brief today. ( logo was delayed)

Target Market(s)

Investors, Corporate , B2b

Industry/Entity Type

real-estate investments

Number of Pages Required

3 page

Requirements
Must have
• Dazzling Homepage
Nice to have
• paralex

```html
<!DOCTYPE html>
<html lang="en">
<head>
<meta charset="utf-8">
<title>Bright Vale Group</title>
<link href="https://fonts.googleapis.com/css2?family=Inter:wght@400;500;600;700&family=Libre+Baskerville:wght@400;700&display=swap" rel="stylesheet">
<style>
:root{
  --ink:#222222;
  --dark:#1f1f1f;
  --sand:#f5cf9a;
  --sand-text:#f3c68c;
  --muted:#f7f7f7;
  --body:#444444;
  --white:#ffffff;
  --serif:'Libre Baskerville', Georgia, serif;
  --sans:'Inter', Arial, sans-serif;
}
*{box-sizing:border-box;margin:0;padding:0}
html,body{width:1200px;height:2908px;overflow:hidden}
body{font-family:var(--sans);color:var(--body);background:var(--white);position:relative}
.abs{position:absolute}

/* top bar */
.topbar{position:absolute;left:0;top:0;width:1200px;height:38px;background:var(--ink)}
.social{position:absolute;left:146px;top:8px;display:flex;gap:10px}
.social span{width:23px;height:23px;border-radius:50%;background:var(--white);display:block}
.top-mail{position:absolute;right:145px;top:11px;color:var(--white);font-size:13px;display:flex;align-items:center;gap:5px}

/* header */
.header{position:absolute;top:38px;left:0;width:1200px;height:86px;background:var(--white)}
.brand{position:absolute;left:140px;top:22px;display:flex;align-items:center;gap:8px;font-family:var(--serif);font-size:24px;color:var(--ink)}
.brand i{width:12px;height:12px;background:var(--ink);display:block}
.search{position:absolute;left:431px;top:21px;width:333px;height:44px;border:1px solid var(--ink);border-radius:22px;display:flex;align-items:center}
.search span{font-size:11px;color:#888;padding-left:16px;flex:1}
.search b{width:124px;height:44px;margin-right:-1px;background:var(--ink);color:var(--white);border-radius:22px;font-size:15px;font-weight:600;display:flex;align-items:center;justify-content:center}
.call{position:absolute;left:816px;top:18px;display:flex;align-items:center;gap:20px}
.call-icon{width:50px;height:50px;border-radius:50%;background:var(--sand);display:flex;align-items:center;justify-content:center}
.call small{display:block;font-size:11.5px;color:#e09a3a;letter-spacing:.2px}
.call strong{display:block;font-family:var(--serif);font-weight:400;font-size:22px;color:var(--ink);margin-top:2px}

/* nav */
.nav{position:absolute;top:124px;left:0;width:1200px;height:48px;background:var(--sand);display:flex;justify-content:center;align-items:center;gap:30px;font-size:13px;font-weight:600;color:var(--ink)}

/* hero */
.hero{position:absolute;top:172px;left:0;width:1200px;height:550px;
  background:linear-gradient(180deg,#7a4a44 0%,#b0664d 22%,#6b4a3a 45%,#5a4a3b 62%,#3f5a2c 82%,#354a25 100%)}
.hero-rule{position:absolute;top:722px;left:0;width:1200px;height:7px;background:var(--sand)}
.hero h1{position:absolute;top:192px;left:0;width:1200px;text-align:center;font-family:var(--serif);font-size:35px;color:var(--white);font-weight:700}
.hero p{position:absolute;top:250px;left:245px;width:710px;text-align:center;color:var(--white);font-size:15px;line-height:28px}
.btn{background:var(--sand);color:var(--ink);font-family:var(--serif);font-weight:700;border-radius:24px;display:flex;align-items:center;justify-content:center;letter-spacing:.5px}
.hero .btn{position:absolute;left:520px;top:318px;width:159px;height:44px;font-size:15px}
.dots{position:absolute;left:575px;top:518px;display:flex;gap:3px}
.dots span{width:8px;height:8px;border-radius:50%;background:var(--white)}
.dots span:nth-child(2){background:var(--sand)}

/* about */
.about{position:absolute;top:729px;left:18px;width:1164px;height:601px;background:var(--muted)}
.sec-title{font-family:var(--serif);font-weight:400;color:var(--ink);font-size:29px;text-align:center}
.bar{width:34px;height:4px;background:var(--ink);margin:0 auto}
.about .sec-title{position:absolute;top:86px;left:0;width:1164px}
.about .bar{position:absolute;top:128px;left:565px}
.about .lead{position:absolute;top:150px;left:0;width:1164px;text-align:center;color:var(--sand-text);font-size:15.5px;font-weight:500}
.about .intro{position:absolute;top:186px;left:172px;width:820px;text-align:center;font-size:14px;line-height:28px}
.feature{position:absolute;top:319px;width:290px;text-align:center}
.feature .ic{width:102px;height:102px;border-radius:50%;background:var(--ink);margin:0 auto;display:flex;align-items:center;justify-content:center}
.feature h3{font-size:16.5px;font-weight:500;color:var(--ink);margin-top:12px}
.feature p{font-size:13px;line-height:28px;margin-top:5px}

/* portfolio */
.portfolio{position:absolute;top:1330px;left:0;width:1200px;height:606px;background:linear-gradient(100deg,#3c3c42 0%,#4a4a52 50%,#6a5a50 100%)}
.portfolio .photo{position:absolute;left:116px;top:80px;width:477px;height:429px;background:linear-gradient(135deg,#eef0f0,#c9ccd0 55%,#8b95a5)}
.portfolio .frame{position:absolute;left:160px;top:97px;width:394px;height:393px;border:15px solid rgba(100,100,100,.75)}
.portfolio h2{position:absolute;left:627px;top:110px;font-family:var(--serif);font-size:29px;color:var(--white);font-weight:700}
.portfolio .bar{position:absolute;left:627px;top:153px;background:var(--white)}
.portfolio h4{position:absolute;left:626px;top:177px;color:var(--white);font-size:16px;font-weight:600}
.portfolio p{position:absolute;left:627px;top:215px;width:460px;color:#eee;font-size:14px;line-height:28px}
.portfolio .btn{position:absolute;left:628px;top:433px;width:166px;height:43px;font-size:14px}

/* blogs */
.blogs .sec-title{position:absolute;top:2043px;left:0;width:1200px;font-weight:700}
.blogs .bar{position:absolute;top:2085px;left:583px}
.card{position:absolute;top:2119px;width:298px;text-align:center}
.card .img{height:212px;border-radius:10px;display:flex;align-items:center;justify-content:center}
.card h3{font-family:var(--serif);font-size:13px;color:var(--ink);line-height:27px;margin-top:12px;font-weight:400;letter-spacing:.3px}
.card p{font-size:13px;line-height:28px;margin-top:8px}
.play{width:42px;height:42px;border-radius:50%;background:rgba(80,80,80,.7);display:flex;align-items:center;justify-content:center}

/* footer */
.foot-rule{position:absolute;top:2540px;left:0;width:1200px;height:7px;background:var(--sand)}
.footer{position:absolute;top:2547px;left:0;width:1200px;height:361px;background:var(--ink);color:var(--white)}
.footer .brand-f{position:absolute;left:145px;top:164px;font-family:var(--serif);font-size:30px;display:flex;align-items:center;gap:10px}
.footer .brand-f i{width:14px;height:14px;background:var(--white);display:block}
.fcol{position:absolute;top:73px}
.fcol h5{font-family:var(--serif);font-size:12.5px;font-weight:700;margin-bottom:22px}
.fcol li{list-style:none;font-size:14px;line-height:24px;display:flex;gap:14px;align-items:flex-start}
.fcol li em{font-style:normal;font-size:12px;width:11px}
.contact li{margin-bottom:11px;line-height:24px}
.footer .rule{position:absolute;left:100px;top:281px;width:967px;height:1px;background:#555}
.copy{position:absolute;top:302px;left:0;width:1200px;text-align:center;font-size:13px}
.copy span{display:inline-block;width:1px;height:16px;background:var(--white);vertical-align:middle;margin:0 14px}
</style>
</head>
<body>

<div class="topbar">
  <div class="social" aria-label="Social links"><span></span><span></span><span></span><span></span><span></span></div>
  <div class="top-mail">
    <svg width="13" height="10" viewBox="0 0 13 10"><rect width="13" height="10" rx="1" fill="#fff"/><path d="M0 1l6.5 5L13 1" stroke="#222" fill="none"/></svg>
    info@bright-vale.net
  </div>
</div>

<header class="header">
  <div class="brand"><i></i>Bright Vale</div>
  <div class="search"><span>Enter here</span><b>SEARCH</b></div>
  <div class="call">
    <div class="call-icon">
      <svg width="20" height="20" viewBox="0 0 24 24"><path d="M6.6 10.8a15 15 0 006.6 6.6l2.2-2.2c.3-.3.7-.4 1-.2 1.1.4 2.3.6 3.6.6.6 0 1 .4 1 1V20c0 .6-.4 1-1 1C10.6 21 3 13.4 3 4c0-.6.4-1 1-1h3.5c.6 0 1 .4 1 1 0 1.3.2 2.5.6 3.6.1.3 0 .7-.2 1z" fill="#222"/></svg>
    </div>
    <div><small>CALL US TODAY</small><strong>123 456 7890</strong></div>
  </div>
</header>

<nav class="nav"><span>HOME</span><span>ABOUT</span><span>TEAM</span><span>PORTFOLIO</span><span>NEWS</span><span>CONTACT US</span></nav>

<section class="hero" role="img" aria-label="Suburban homes on a green lawn under a sunset sky">
  <h1>LOREM IPSUM DOLOR SIT AMET CONSE</h1>
  <p>Lorem ipsum dolor sit amet, consectetur adipiscing elit, sed do eiusmod tempor incididunt ut labore et dolore magna aliqua.</p>
  <div class="btn">GET STARTED</div>
  <div class="dots"><span></span><span></span><span></span><span></span><span></span></div>
</section>
<div class="hero-rule"></div>

<section class="about">
  <h2 class="sec-title">ABOUT BRIGHT VALE</h2>
  <div class="bar"></div>
  <div class="lead">LOREM IPSUM DOLOR SIT AMET, CONSECTETUR ADIPISCING ELIT</div>
  <p class="intro">Lorem ipsum dolor sit amet, consectetur adipiscing elit, sed do eiusmod tempor incididunt ut labore et dolore magna aliqua. Ut enim ad minim veniam, quis nostrud exercitation ullamco laboris nisi ut aliquip ex ea commodo consequat. Duis aute irure dolor in reprehenderit in voluptate velit esse cillum dolore eu fugiat nulla pariatur. Excepteur sint occaecat cupidatat non proident, sunt in culpa qui officia deserunt mollit anim id est laborum</p>

  <div class="feature" style="left:127px">
    <div class="ic"><svg width="56" height="50" viewBox="0 0 56 50" fill="none" stroke="#fff" stroke-width="2"><rect x="4" y="8" width="48" height="30" rx="2"/><path d="M22 38v6h12v-6M16 46h24M12 30h20M12 24h14"/><path d="M34 28l10-14 4 3-10 14z"/></svg></div>
    <h3>REAL ESTATE</h3>
    <p>Lorem ipsum dolor sit amet, consectetur adipiscing elit, sed do eiusmod tempor incididunt ut labore et dolore magna</p>
  </div>
  <div class="feature" style="left:441px">
    <div class="ic"><svg width="50" height="50" viewBox="0 0 50 50" fill="none" stroke="#fff" stroke-width="2"><path d="M6 10h30v34H6zM12 16v22h20zM40 6v30l3 5 3-5V6z"/><path d="M17 30h5v5"/></svg></div>
    <h3>INVESTMENT</h3>
    <p>Lorem ipsum dolor sit amet, consectetur adipiscing elit, sed do eiusmod tempor incididunt ut labore et dolore magna</p>
  </div>
  <div class="feature" style="left:753px">
    <div class="ic"><svg width="46" height="52" viewBox="0 0 46 52" fill="none" stroke="#fff" stroke-width="2.2"><path d="M16 4h14v18h9L23 40 7 22h9z"/><path d="M4 30v18h38V30"/></svg></div>
    <h3>FINANCIAL CORPORATE</h3>
    <p>Lorem ipsum dolor sit amet, consectetur adipiscing elit, sed do eiusmod tempor incididunt ut labore et dolore magna</p>
  </div>
</section>

<section class="portfolio">
  <div class="photo" role="img" aria-label="Couple viewing a bright home with an agent holding a tablet"></div>
  <div class="frame"></div>
  <h2>OUR PORTFOLIO</h2>
  <div class="bar"></div>
  <h4>LOREM IPSUM DOLOR SIT AMET, CONSECTETUR ADIPISCING</h4>
  <p>Lorem ipsum dolor sit amet, consectetur adipiscing elit, sed do eius-mod tempor incididunt ut labore et dolore magna aliqua. Ut enim ad minim veniam, quis nostrud exercitation ullamco laboris nisi ut aliquip ex ea commodo consequat. Duis aute irure dolor in reprehenderit in voluptate velit esse cillum dolore eu fugiat nulla pariatur. Excepteur sint occaecat cupidatat non proident, sunt in culpa qui officia deserunt mollit anim id est laborum.</p>
  <div class="btn">LEARN MORE</div>
</section>

<section class="blogs">
  <h2 class="sec-title">OUR LATEST BLOGS</h2>
  <div class="bar"></div>

  <article class="card" style="left:128px">
    <div class="img" role="img" aria-label="Advisor meeting clients at a laptop" style="background:linear-gradient(135deg,#b9b4b4,#6d6a6a 60%,#3e4b5c)">
      <div class="play"><svg width="16" height="16" viewBox="0 0 16 16"><path d="M4 2l10 6-10 6z" fill="#fff"/></svg></div>
    </div>
    <h3>LOREM IPSUM DOLOR SIT AMET<br>ETUR ADIPISCING ELIT</h3>
    <p>Lorem ipsum dolor sit amet, consectetur adip-iscing elit, sed do eiusmod tempor incididunt ut labore et dolore magna aliqua.</p>
  </article>
  <article class="card" style="left:451px">
    <div class="img" role="img" aria-label="Handshake over a small wooden house model" style="background:linear-gradient(135deg,#2e2a28,#6a5a4c 50%,#c9a27c)">
      <div class="play"><svg width="16" height="16" viewBox="0 0 16 16"><path d="M4 2l10 6-10 6z" fill="#fff"/></svg></div>
    </div>
    <h3>LOREM IPSUM DOLOR SIT AMET<br>ETUR ADIPISCING ELIT</h3>
    <p>Lorem ipsum dolor sit amet, consectetur adip-iscing elit, sed do eiusmod tempor incididunt ut labore et dolore magna aliqua.</p>
  </article>
  <article class="card" style="left:774px">
    <div class="img" role="img" aria-label="Desk with house model and charts during a business meeting" style="background:linear-gradient(135deg,#5a5a5a,#8b8178 50%,#3f4c63)"></div>
    <h3>LOREM IPSUM DOLOR SIT AMET<br>ETUR ADIPISCING ELIT</h3>
    <p>Lorem ipsum dolor sit amet, consectetur adip-iscing elit, sed do eiusmod tempor incididunt ut labore et dolore magna aliqua.</p>
  </article>
</section>

<div class="foot-rule"></div>
<footer class="footer">
  <div class="brand-f"><i></i>Bright Vale</div>
  <div class="fcol" style="left:440px">
    <h5>QUICK LINKS</h5>
    <ul><li><em>»</em>Home</li><li><em>»</em>About</li><li><em>»</em>Team</li><li><em>»</em>Portfolio</li><li><em>»</em>News</li></ul>
  </div>
  <div class="fcol" style="left:641px">
    <h5>IMPORTANT</h5>
    <ul><li><em>»</em>Privacy Policy</li><li><em>»</em>Terms &amp; Conditions</li><li><em>»</em>Contact Us</li><li><em>»</em>About Us</li></ul>
  </div>
  <div class="fcol contact" style="left:855px">
    <h5>CONTACT INFO</h5>
    <ul>
      <li><em><svg width="10" height="14" viewBox="0 0 10 14"><path d="M5 0a5 5 0 00-5 5c0 4 5 9 5 9s5-5 5-9a5 5 0 00-5-5zm0 7a2 2 0 110-4 2 2 0 010 4z" fill="#fff"/></svg></em>Lorem ipsum dolor sit<br>amet, consectetur</li>
      <li><em><svg width="12" height="12" viewBox="0 0 24 24"><path d="M6.6 10.8a15 15 0 006.6 6.6l2.2-2.2c.3-.3.7-.4 1-.2 1.1.4 2.3.6 3.6.6.6 0 1 .4 1 1V20c0 .6-.4 1-1 1C10.6 21 3 13.4 3 4c0-.6.4-1 1-1h3.5c.6 0 1 .4 1 1 0 1.3.2 2.5.6 3.6.1.3 0 .7-.2 1z" fill="#fff"/></svg></em>1 888 888 8888</li>
      <li><em><svg width="13" height="10" viewBox="0 0 13 10"><rect width="13" height="10" rx="1" fill="#fff"/><path d="M0 1l6.5 5L13 1" stroke="#222" fill="none"/></svg></em>info@bright-vale.net</li>
    </ul>
  </div>
  <div class="rule"></div>
  <div class="copy">© Copyrights 2021 Bright Vale<span></span>All Rights Reserved</div>
</footer>

</body>
</html>
```